Craft oriented film company needs a Business Card design

Hi all,
We're a 2-man band film company in New Zealand called Kestrel Pictures. We're good honest blokes, who are very passionate about the craft of film making. I've attached our current logo which has a bit of a crafty/artisan feel that we like. Feel free to use it - or throw the baby out with the bathwater and start again..... you never know, you might inspire a complete brand re-work.

In any case, the vibe we want to give out is that we are solid, dependable and no bullshit - but without compromising creative excellence and being in the now. We like the 'Brooklyn' artisan style of work.

Preferably single sided.

We need the standard stuff:
Name, job title, cellphone, email address and physical address (this can be smaller if you like - street, suburb, city & zip, country [if you want])

Check out our website to learn more about us: kestrelpictures.example

Target Market(s)

Brand marketers and advertising agency creatives looking for video production.

Industry/Entity Type

Baby

Requirements
Should not have
• Nothing flashy or too 'futuristic', we want it to feel grounded and real. A limited colour palette is preferred.
We don't want any film reels or cameras or anything obvious like that.

```html
<!DOCTYPE html>
<html lang="en">
<head>
<meta charset="utf-8">
<title>Kestrel Pictures – Business Cards</title>
<link rel="stylesheet" href="https://fonts.googleapis.com/css2?family=Gelasio:wght@400;700&display=swap">
<style>
  :root {
    --page: #ffffff;
    --card-light: #5e5e5e;
    --card-mid: #3a3a3a;
    --card-dark: #000000;
    --badge: #0b0b0b;
    --badge-ring: #f2f2f2;
    --tab-orange: #f5a53c;
    --tab-yellow: #fedb1a;
    --name-ink: #151515;
    --muted: #a9a9a9;
    --contact: #bdbdbd;
    --back-mark: rgba(0, 0, 0, 0.28);
    --back-word: #767676;
  }
  * { box-sizing: border-box; margin: 0; padding: 0; }
  html, body {
    width: 1200px; height: 768px; overflow: hidden;
    background: var(--page);
    font-family: "Gelasio", Georgia, serif;
  }
  .sheet { position: relative; width: 1200px; height: 768px; }

  .card {
    position: absolute; width: 576px; height: 359px; overflow: hidden;
    background: linear-gradient(162deg, var(--card-light) 0%, var(--card-mid) 42%, var(--card-dark) 78%);
  }
  .card--front-a { left: 0; top: 0; }
  .card--front-b { left: 0; top: 410px; height: 358px; }
  .card--back-a { left: 624px; top: 0; }
  .card--back-b { left: 624px; top: 410px; height: 358px; }

  /* front */
  .badge {
    position: absolute; left: 30px; top: 22px; width: 122px; height: 122px;
    border-radius: 50%; background: var(--badge);
    box-shadow: 0 0 0 3px var(--badge-ring) inset, 0 0 0 2px var(--badge) inset;
    display: flex; align-items: center; justify-content: center; text-align: center;
  }
  .badge__name {
    color: var(--badge-ring); font-weight: 700; font-size: 17px; line-height: 1.15;
  }
  .name-shadow {
    position: absolute; left: 185px; top: 52px; width: 22px; height: 90px;
    background: linear-gradient(90deg, rgba(0,0,0,0.55), rgba(0,0,0,0));
  }
  .name-tab {
    position: absolute; left: 187px; top: 63px; width: 226px; height: 43px;
    border-radius: 0 22px 22px 0;
    background: linear-gradient(90deg, var(--tab-orange) 0%, var(--tab-yellow) 45%, var(--tab-yellow) 100%);
    display: flex; align-items: center; padding-left: 12px;
  }
  .name-tab__name { color: var(--name-ink); font-size: 27px; line-height: 1; }
  .role {
    position: absolute; left: 318px; top: 110px;
    color: var(--muted); font-size: 17px;
  }
  .contact {
    position: absolute; left: 198px; top: 172px;
    list-style: none; color: var(--contact); font-size: 12px; line-height: 15px;
  }
  .contact__sector { font-weight: 700; }
  .address {
    position: absolute; left: 413px; top: 174px;
    color: var(--contact); font-size: 10px; line-height: 13px; font-weight: 700;
    font-style: normal; text-align: center;
  }

  /* back */
  .back-mark {
    position: absolute; left: 54px; top: -30px; width: 440px; height: 440px;
    border-radius: 50%; background: var(--back-mark);
  }
  .back-word {
    position: absolute; left: 54px; top: 110px; width: 440px; text-align: center;
    color: var(--back-word); font-weight: 700; font-size: 56px; line-height: 1.05;
  }
</style>
</head>
<body>
<main class="sheet">

  <section class="card card--front-a" aria-label="Business card front, Rowan Tate">
    <div class="badge"><span class="badge__name">Kestrel<br>Pictures</span></div>
    <div class="name-shadow"></div>
    <div class="name-tab"><h1 class="name-tab__name">Rowan Tate</h1></div>
    <p class="role">Producer</p>
    <ul class="contact">
      <li>(64) 21-555-010</li>
      <li>rowan@kestrelpictures.example</li>
      <li>www.kestrelpictures.example</li>
      <li class="contact__sector">Arts &amp; Entertainment</li>
      <li class="contact__sector">Broadcasting &amp; Media Production</li>
    </ul>
    <address class="address">12 Kowhai st, west lane,<br>auckland, new zealand 1000</address>
  </section>

  <section class="card card--back-a" aria-label="Business card back">
    <div class="back-mark"></div>
    <p class="back-word">Kestrel<br>Pictures</p>
  </section>

  <section class="card card--front-b" aria-label="Business card front, Miles Hartley">
    <div class="badge"><span class="badge__name">Kestrel<br>Pictures</span></div>
    <div class="name-shadow"></div>
    <div class="name-tab"><h1 class="name-tab__name">Miles Hartley</h1></div>
    <p class="role">Director</p>
    <ul class="contact">
      <li>(64) 21-555-020</li>
      <li>miles@kestrelpictures.example</li>
      <li>www.kestrelpictures.example</li>
      <li class="contact__sector">Arts &amp; Entertainment</li>
      <li class="contact__sector">Broadcasting &amp; Media Production</li>
    </ul>
    <address class="address">12 Kowhai st, west lane,<br>auckland, new zealand 1000</address>
  </section>

  <section class="card card--back-b" aria-label="Business card back">
    <div class="back-mark"></div>
    <p class="back-word">Kestrel<br>Pictures</p>
  </section>

</main>
</body>
</html>
```